Love Your Hearing - Life Sounds Good

I need a website. I had a company doing it, and it looked very nice, but they went way up on hosting costs and said they owned the design of the site. I changed hosts to keep costs down. You can see the current design at crestvaleaudio.com. They said I could use the copy and images from the current website. So you could cut and paste to speed things up. My logo and other images are on the current website. If you are unable to use I can send other digital copies.

Target Market(s)

seniors 55 and up

Number of Pages Required

4 page

Font styles to use
Sans Serif

Colors
0255a3
f78f20

Requirements
Must have
• Video testimonies that I can add without assistance. I use youtube links for the videos.
Nice to have
• The color scheme theme can be drawn from the logo, which is on the current webstie crestvaleaudio.com
Should not have
• Should not have anything related to SonoPath on the website.

```html
<!DOCTYPE html>
<html lang="en">
<head>
<meta charset="utf-8">
<title>Crestvale Hearing Center</title>
<link rel="stylesheet" href="https://fonts.googleapis.com/css2?family=Roboto:wght@400;500;700&family=Open+Sans:wght@400;600&display=swap">
<style>
:root{
  --blue:#0255a3;
  --orange:#f78f20;
  --ink:#222;
  --text:#444;
  --muted:#888;
  --light:#f2f2f2;
  --dark:#232323;
  --white:#fff;
}
*{box-sizing:border-box;margin:0;padding:0}
html,body{width:1200px;height:4559px;overflow:hidden}
body{font-family:"Open Sans",sans-serif;color:var(--text);background:var(--white);position:relative}
.section{position:absolute;left:0;width:1200px}
.abs{position:absolute}
.heading{font-family:"Roboto",sans-serif;font-weight:700}
.center{text-align:center;left:0;width:1200px}

/* header */
.site-header{top:0;height:135px;background:var(--white)}
.social{width:26px;height:26px;border-radius:50%;background:var(--blue);top:38px}
.topline{height:1px;background:var(--blue);top:78px}
.header-link{font-family:"Roboto",sans-serif;font-size:14px;color:#333;top:43px}
.nav a{position:absolute;top:98px;font-family:"Roboto",sans-serif;font-size:14px;color:#444;text-decoration:none}
.brand{left:508px;top:52px;display:flex;align-items:center;gap:10px}
.brand-mark{width:44px;height:44px;background:var(--orange)}
.brand-name{font-family:"Roboto",sans-serif;font-weight:700;font-size:19px;color:var(--blue);line-height:1.1}
.search{left:935px;top:36px;width:175px;height:34px;border:1px solid var(--blue);border-radius:17px;font-size:13px;color:var(--muted);padding:8px 0 0 18px}
.search-btn{position:absolute;right:2px;top:2px;width:30px;height:28px;border-radius:0 14px 14px 0;background:var(--blue)}

/* hero */
.hero{top:135px;height:592px;background:linear-gradient(110deg,#3a3f4a 0%,#8a6a56 35%,#a8a39a 65%,#3f4a58 100%)}
.hero-title{right:90px;top:180px;font-size:52px;color:var(--white);text-align:right}
.hero-sub{right:90px;top:252px;font-family:"Roboto",sans-serif;font-size:29px;color:var(--white);font-weight:500}
.hero-btn{right:90px;top:318px;width:265px;height:65px;border:2px solid var(--white);border-radius:4px;color:var(--white);font-family:"Roboto",sans-serif;font-size:25px;display:flex;align-items:center;justify-content:center}

/* welcome */
.welcome{top:727px;height:525px;background:var(--light)}
.section-title{font-size:40px;color:var(--blue)}
.welcome-text{left:145px;width:910px;top:118px;font-size:16px;line-height:27px;text-align:center;color:#555}
.service-tile{width:205px;height:148px;background:var(--white);border:2px solid #ddd;border-radius:6px;display:flex;align-items:center;justify-content:center}
.service-tile.active{background:var(--orange);border-color:var(--orange)}
.service-label{width:240px;text-align:center;font-family:"Roboto",sans-serif;font-weight:700;font-size:21px;color:var(--ink);line-height:27px}

/* doctor */
.doctor{top:1252px;height:606px}
.doctor-name{left:88px;top:66px;font-size:40px;color:var(--ink)}
.doctor-org{left:88px;top:120px;font-family:"Roboto",sans-serif;font-size:24px;color:var(--blue)}
.doctor-quote{left:90px;top:172px;width:510px;font-size:17px;line-height:27px;color:#555}
.btn{background:var(--orange);color:var(--white);font-family:"Roboto",sans-serif;display:flex;align-items:center;justify-content:center;border-radius:4px}
.doctor-btn{left:90px;top:478px;width:190px;height:56px;font-size:19px}
.doctor-photo{left:728px;top:45px;width:383px;height:483px;background:linear-gradient(180deg,#eef2f5 0%,#d9dee3 55%,#b9c2cc 100%)}

/* ways */
.ways{top:1858px;height:486px;background:linear-gradient(120deg,#1a63aa 0%,#2470b4 50%,#1c66ad 100%)}
.ways-title{top:56px;font-size:40px;color:var(--white);font-weight:500}
.ways-by{top:110px;font-family:"Roboto",sans-serif;font-size:23px;color:var(--white);font-weight:500}
.way-card{top:217px;width:212px;height:140px;background:var(--white);border-radius:4px;display:flex;align-items:center;justify-content:center}
.way-label{top:382px;width:212px;text-align:center;font-family:"Roboto",sans-serif;font-size:22px;color:var(--white);font-weight:500}
.arrow{width:22px;height:22px}

/* news */
.news{top:2344px;height:773px}
.news-title{top:82px;font-size:42px;color:var(--blue)}
.news-sub{top:157px;font-size:15px;color:#333}
.news-sub span{color:var(--orange);text-decoration:underline}
.news-card{top:223px;width:310px;height:455px;border:1px solid #ddd;box-shadow:0 0 6px rgba(0,0,0,.25);background:var(--white)}
.news-img{position:absolute;left:8px;top:8px;width:292px;height:165px}
.news-date{position:absolute;left:14px;top:14px;color:var(--white);font-size:15px}
.news-head{position:absolute;left:12px;width:284px;top:192px;text-align:center;font-family:"Roboto",sans-serif;font-weight:700;font-size:19px;line-height:27px;color:var(--blue)}
.news-body{position:absolute;left:12px;width:284px;top:284px;text-align:center;font-size:14.5px;line-height:21px;color:#444}
.news-btn{position:absolute;left:100px;top:406px;width:114px;height:30px;border-radius:10px;font-size:14px}

/* videos */
.videos{top:3117px;height:446px;background:var(--orange)}
.videos-title{top:52px;font-size:40px;color:var(--white);font-weight:500}
.video{top:156px;width:300px;height:192px}
.play{position:absolute;left:135px;top:81px;width:32px;height:32px;border-radius:50%;background:var(--white)}
.play::after{content:"";position:absolute;left:12px;top:9px;border-left:11px solid #111;border-top:7px solid transparent;border-bottom:7px solid transparent}
.video-name{top:370px;width:300px;text-align:center;font-family:"Roboto",sans-serif;font-size:24px;color:var(--white);font-weight:500}

/* quote */
.quote{top:3563px;height:561px;background:#f7f7f7}
.quote-title{left:213px;top:30px;font-size:38px;color:var(--blue)}
.field{left:88px;width:495px;height:45px;background:var(--white);border:1px solid #ddd;font-size:12px;color:var(--muted);padding:14px 0 0 12px}
.submit{left:88px;top:487px;width:119px;height:37px;font-size:16px}
.map{left:608px;top:0;width:592px;height:561px;background:linear-gradient(160deg,#f1f0ec 0%,#ecebe6 50%,#e6e5e0 100%)}

/* footer */
.site-footer{top:4124px;height:435px;background:var(--dark);color:var(--white)}
.footer-brand{left:90px;top:170px;display:flex;align-items:center;gap:14px}
.footer-mark{width:72px;height:72px;background:var(--white)}
.footer-name{font-family:"Roboto",sans-serif;font-weight:700;font-size:30px;line-height:1.05;color:var(--white)}
.footer-head{top:86px;font-size:26px;font-weight:500}
.footer-list{top:150px;font-size:15.5px;line-height:27px}
.footer-contact{top:150px;font-size:15.5px;line-height:32px}
.news-input{left:880px;top:246px;width:230px;height:36px;border:1px solid #bbb;border-radius:5px;font-size:12px;color:var(--white);padding:10px 0 0 14px}
.send{left:880px;top:304px;width:122px;height:34px;font-size:16px}
.copyright{top:391px;font-family:"Roboto",sans-serif;font-size:17px}
</style>
</head>
<body>

<header class="section site-header">
  <div class="abs social" style="left:90px"></div>
  <div class="abs social" style="left:124px"></div>
  <div class="abs header-link" style="left:210px">Welcome&nbsp;|&nbsp;&nbsp;Reviews</div>
  <div class="abs topline" style="left:90px;width:402px"></div>
  <div class="abs brand">
    <div class="brand-mark"></div>
    <div class="brand-name">CRESTVALE<br>HEARING CENTER</div>
  </div>
  <svg class="abs" style="left:716px;top:41px" width="20" height="20" viewBox="0 0 24 24"><path fill="#0255a3" d="M6.6 10.8a15.1 15.1 0 0 0 6.6 6.6l2.2-2.2a1 1 0 0 1 1-.25 11.4 11.4 0 0 0 3.6.57 1 1 0 0 1 1 1V20a1 1 0 0 1-1 1A17 17 0 0 1 3 4a1 1 0 0 1 1-1h3.5a1 1 0 0 1 1 1c0 1.250.2 2.450.57 3.57a1 1 0 0 1-.25 1z"/></svg>
  <div class="abs header-link" style="left:750px">(555) 214-0386</div>
  <div class="abs search">Search...<div class="search-btn">
    <svg width="30" height="28" viewBox="0 0 30 28"><circle cx="14" cy="13" r="5" fill="none" stroke="#fff" stroke-width="2"/><line x1="18" y1="17" x2="21" y2="20" stroke="#fff" stroke-width="2"/></svg>
  </div></div>
  <div class="abs topline" style="left:708px;width:402px"></div>
  <nav class="nav">
    <a style="left:147px">Home</a>
    <a style="left:218px">Hearing Aids</a>
    <a style="left:335px">Services</a>
    <a style="left:726px">Education</a>
    <a style="left:823px">About Us</a>
    <a style="left:916px">Contact Us</a>
  </nav>
</header>

<section class="section hero" role="img" aria-label="Photo of a smiling mother and daughter cheek to cheek, a white flower in the girl's hair">
  <h1 class="abs heading hero-title">Recapture The Sounds Of Life</h1>
  <p class="abs hero-sub">and the intimacy of a quiet conversation</p>
  <div class="abs hero-btn">Take Action Today</div>
</section>

<section class="section welcome">
  <h2 class="abs heading center section-title" style="top:55px">Welcome to Crestvale Hearing</h2>
  <p class="abs welcome-text">We provide hearing evaluations, counseling, and fitting of hearing aids. We service all the major brands of hearing aids including Auralis, ClearTone, Vantra, Sonella, Hearwell, Nuvox, MicroPulse, Unisound, Tonique, Brightear, Halcyon, and others.</p>

  <div class="abs service-tile" style="left:90px;top:248px">
    <svg width="90" height="110" viewBox="0 0 90 110" fill="none" stroke="#0255a3" stroke-width="4" stroke-linecap="round"><rect x="8" y="8" width="26" height="34" rx="13"/><rect x="56" y="8" width="26" height="34" rx="13"/><circle cx="21" cy="25" r="5"/><path d="M21 42v60M69 42v60M34 30l10 4M56 30l-10 4"/></svg>
  </div>
  <div class="abs service-label" style="left:72px;top:423px">Brands</div>

  <div class="abs service-tile active" style="left:378px;top:248px">
    <svg width="100" height="100" viewBox="0 0 100 100" fill="none" stroke="#fff" stroke-width="5" stroke-linecap="round"><path d="M18 18l64 64M82 82l-6 6M14 24l10-10"/><path d="M82 18L30 70M22 78a8 8 0 1 0 8-8M78 10a12 12 0 0 0-8 16l12 0a12 12 0 0 0-4-16"/></svg>
  </div>
  <div class="abs service-label" style="left:360px;top:418px">Repairs /<br>Maintenance</div>

  <div class="abs service-tile" style="left:645px;top:246px">
    <svg width="70" height="100" viewBox="0 0 70 100" fill="none" stroke="#0255a3" stroke-width="4"><rect x="8" y="12" width="54" height="84" rx="5"/><rect x="24" y="4" width="22" height="8"/><path d="M20 34h30M20 48h30M20 62h30M20 76h30"/></svg>
  </div>
  <div class="abs service-label" style="left:627px;top:418px">Batteries</div>

  <div class="abs service-tile" style="left:908px;top:246px">
    <svg width="100" height="100" viewBox="0 0 100 100" fill="none" stroke="#0255a3" stroke-width="4" stroke-linecap="round"><rect x="58" y="8" width="12" height="20" rx="6"/><path d="M64 28c0 30 20 40 0 54c-14 10-34 4-34-10c0-10 0-18 0-28"/><rect x="22" y="30" width="14" height="26" rx="7"/></svg>
  </div>
  <div class="abs service-label" style="left:888px;top:423px">Featured<br>Technology</div>
</section>

<section class="section doctor">
  <h2 class="abs heading doctor-name">Dr. Martin Hollis</h2>
  <p class="abs doctor-org">Crestvale Hearing Center LLC</p>
  <p class="abs doctor-quote">"I was first introduced to hearing aids as a patient. At the tender age of 36, I was diagnosed with profound hearing loss by a hearing healthcare provider in Raleigh, North Carolina. I was fitted with two in-the-ear hearing aids that instantly changed my life! There was no more straining to hear what people were saying, and no more trying to piece together a discussion to make sense of the conversation. Now I could relax and enjoy the pleasant sounds of music and conversation. I actually had more confidence and energy at the end of the work day."</p>
  <div class="abs btn doctor-btn">Read More</div>
  <div class="abs doctor-photo" role="img" aria-label="Portrait of the doctor in a white coat with arms crossed"></div>
</section>

<section class="section ways">
  <h2 class="abs heading center ways-title">50 Ways to Love Your Hearing</h2>
  <p class="abs center ways-by">by Marty Hollis</p>
  <svg class="abs arrow" style="left:33px;top:287px" viewBox="0 0 22 22" fill="none" stroke="#fff" stroke-width="2"><circle cx="11" cy="11" r="9"/><path d="M15 11H7M10 8l-3 3 3 3"/></svg>
  <svg class="abs arrow" style="left:1144px;top:287px" viewBox="0 0 22 22" fill="none" stroke="#fff" stroke-width="2"><circle cx="11" cy="11" r="9"/><path d="M7 11h8M12 8l3 3-3 3"/></svg>

  <div class="abs way-card" style="left:122px">
    <svg width="100" height="90" viewBox="0 0 100 90" fill="none" stroke="#0255a3" stroke-width="3" stroke-linecap="round"><circle cx="74" cy="22" r="14"/><path d="M63 31L14 76l8 8 45-49M10 80l-4 4"/></svg>
  </div>
  <div class="abs way-label" style="left:122px">Singing</div>

  <div class="abs way-card" style="left:363px">
    <svg width="100" height="100" viewBox="0 0 100 100" fill="none" stroke="#0255a3" stroke-width="3"><ellipse cx="24" cy="80" rx="13" ry="10"/><ellipse cx="72" cy="70" rx="13" ry="10"/><path d="M37 80V20l48-10v60M37 34l48-10"/></svg>
  </div>
  <div class="abs way-label" style="left:363px">Music</div>

  <div class="abs way-card" style="left:605px">
    <svg width="120" height="110" viewBox="0 0 120 110" fill="none" stroke="#0255a3" stroke-width="3" stroke-linecap="round"><path d="M14 14l4 10 10 4-10 4-4 10-4-10-10-4 10-4zM96 80l3 7 7 3-7 3-3 7-3-7-7-3 7-3z"/><circle cx="50" cy="30" r="7"/><circle cx="80" cy="18" r="7"/><path d="M50 37v30l-10 30M50 67l12 30M40 46l-14 10M50 46l16-10M80 25v30l-6 26M80 55l10 26M80 34l14 12"/></svg>
  </div>
  <div class="abs way-label" style="left:605px">Dancing</div>

  <div class="abs way-card" style="left:847px">
    <svg width="110" height="110" viewBox="0 0 110 110" fill="none" stroke="#0255a3" stroke-width="2.5"><path fill="#0255a3" d="M20 62c10 14 36 18 50 6 8-6 8-18 16-20-6-4-14-2-18 4-6-10-18-14-30-4 0 8-6 14-18 14z"/><path d="M56 76l-4 12M62 74l2 12"/><path d="M74 22v14M74 22l8-2v12M94 34v12l8-2v-10"/><circle cx="72" cy="36" r="3" fill="#0255a3"/><circle cx="80" cy="32" r="3" fill="#0255a3"/><circle cx="92" cy="46" r="3" fill="#0255a3"/></svg>
  </div>
  <div class="abs way-label" style="left:847px">Bird Song</div>
</section>

<section class="section news">
  <h2 class="abs heading center news-title">What's New in Hearing Health?</h2>
  <p class="abs center news-sub">Learn more about hearing healthcare through the articles below; <span>click here to subscribe.</span></p>

  <article class="abs news-card" style="left:98px">
    <div class="news-img" role="img" aria-label="Photo of an older couple laughing together" style="background:linear-gradient(135deg,#c9c3b8,#8d8a80)"></div>
    <div class="news-date">12/19/2018</div>
    <h3 class="news-head">Do's and Don'ts for Communicating During the Holidays</h3>
    <p class="news-body">It's important to make sure that everyone is comfortable and getting what they need in large group settings, and using these tips for communicating with people.</p>
    <div class="btn news-btn">Read More</div>
  </article>

  <article class="abs news-card" style="left:443px">
    <div class="news-img" role="img" aria-label="Photo of a family in a canoe on a lake" style="background:linear-gradient(180deg,#5c544c,#8a7a6a 55%,#a0423e)"></div>
    <div class="news-date">6.01.2018</div>
    <h3 class="news-head">Communication for All: How People of All Ages Benefit from Better Hearing</h3>
    <p class="news-body">Regardless of age, occupation or gender everyone can benefit from clear communication and healthy hearing. Check out this article, crafted to celebrate Better.</p>
    <div class="btn news-btn">Read More</div>
  </article>

  <article class="abs news-card" style="left:788px">
    <div class="news-img" role="img" aria-label="Photo of a hearing specialist fitting a hearing aid" style="background:linear-gradient(135deg,#7e8a96,#b8a49a 60%,#c0483c)"></div>
    <div class="news-date">9.14.2017</div>
    <h3 class="news-head">Over-the-Counter Hearing Aids: What You Need to Know</h3>
    <p class="news-body">In August 2017, a law was passed that allows FDA-regulated hearing aids to be sold over the counter instead of by a trained hearing healthcare professional.</p>
    <div class="btn news-btn">Read More</div>
  </article>
</section>

<section class="section videos">
  <h2 class="abs heading center videos-title">Video Testimonials</h2>
  <svg class="abs arrow" style="left:35px;top:243px" viewBox="0 0 22 22" fill="none" stroke="#fff" stroke-width="2"><circle cx="11" cy="11" r="9"/><path d="M15 11H7M10 8l-3 3 3 3"/></svg>
  <svg class="abs arrow" style="left:1142px;top:243px" viewBox="0 0 22 22" fill="none" stroke="#fff" stroke-width="2"><circle cx="11" cy="11" r="9"/><path d="M7 11h8M12 8l3 3-3 3"/></svg>

  <div class="abs video" style="left:90px;background:linear-gradient(135deg,#6d6a66,#a39c92)" role="img" aria-label="Video still of a patient giving a testimonial"><div class="play"></div></div>
  <div class="abs video-name" style="left:90px">Grant</div>
  <div class="abs video" style="left:448px;background:linear-gradient(135deg,#7a7770,#b0aaa0)" role="img" aria-label="Video still of a patient giving a testimonial"><div class="play"></div></div>
  <div class="abs video-name" style="left:448px">Walter Price</div>
  <div class="abs video" style="left:808px;background:linear-gradient(135deg,#8b8580,#c4beb6)" role="img" aria-label="Video still of a patient giving a testimonial"><div class="play"></div></div>
  <div class="abs video-name" style="left:808px">Lorraine</div>
</section>

<section class="section quote">
  <h2 class="abs heading quote-title">Get A Quote</h2>
  <div class="abs field" style="top:107px">Name</div>
  <div class="abs field" style="top:179px">Email</div>
  <div class="abs field" style="top:247px">Address</div>
  <div class="abs field" style="top:317px;height:135px">Message</div>
  <div class="abs btn submit">Submit</div>
  <div class="abs map" role="img" aria-label="Street map showing the clinic location"></div>
</section>

<footer class="section site-footer">
  <div class="abs footer-brand">
    <div class="footer-mark"></div>
    <div class="footer-name">CRESTVALE<br>HEARING CENTER</div>
  </div>
  <h3 class="abs heading footer-head" style="left:460px">Quick Links</h3>
  <ul class="abs footer-list" style="left:460px;list-style:none">
    <li>Home</li><li>Hearing Aids</li><li>Services</li><li>Education</li><li>About Us</li><li>Contact Us</li>
  </ul>
  <h3 class="abs heading footer-head" style="left:642px">Contact Us</h3>
  <div class="abs footer-contact" style="left:642px">240 Elm Ridge Rd Suite 12<br>Crestvale, NC 28099<br>(555) 214-0386<br>info@crestvaleaudio.com</div>
  <h3 class="abs heading footer-head" style="left:880px">Newsletter</h3>
  <p class="abs" style="left:882px;top:152px;width:200px;font-size:15.5px;line-height:21px">Hear what our patients have to say in their own words</p>
  <div class="abs news-input">Enter The Email</div>
  <div class="abs btn send">Send</div>
  <p class="abs center copyright">© 2019 Crestvale Hearing Center LLC Healthcare</p>
</footer>

</body>
</html>
```